Company Website for Vortel Insight, an open source data analytics company focused on relationship and li

I need a company/brand website for our new startup, Vortel Insight LLC. We are a company focused on using life pattern analysis techniques, looking at relationships and how relationships, attributes, and activity cluster to infer aggregate information about individuals and groups. Our focus is on improving the digital advertising market.

We have a company logo which I will upload shortly.

Target Market(s)

Digital Advertising

Number of Pages Required

3 page

Font styles to use
Sans Serif

Requirements
Must have
• An main page, about us, contact page.
Nice to have
• Vortel Insight relies on state of the art analytics applied to a the digital marketing space. While it is heavy in science, we also understand the art of influence. The website should have a scientific edge but also a flair that illustrates our focus on applying the hard science and analytics to influencing the behavior of people.

```html
<!DOCTYPE html>
<html lang="en">
<head>
<meta charset="utf-8">
<title>Vortel Insight</title>
<link href="https://fonts.googleapis.com/css2?family=Poppins:wght@400;500;600&display=swap" rel="stylesheet">
<style>
:root{
  --blue:#1f73bf;
  --orange:#f7931e;
  --orange-soft:#fdd6a4;
  --ink:#111;
  --muted:#666;
  --white:#fff;
  --field-line:#e4e4e4;
}
*{box-sizing:border-box;margin:0;padding:0}
html,body{width:1200px;height:2826px;overflow:hidden;background:var(--white)}
body{position:relative;font-family:"Poppins",Arial,sans-serif;color:var(--ink)}
.abs{position:absolute}
.shape{position:absolute;left:0;top:0}
.brand{font-weight:600;font-size:26px;color:var(--blue);display:flex;align-items:center;gap:10px}
.brand-dot{width:14px;height:14px;border-radius:50%;background:var(--orange)}
.nav a{position:absolute;top:46px;color:var(--white);font-size:15px;text-decoration:none}
.btn{position:absolute;display:flex;align-items:center;justify-content:center;border-radius:24px;font-size:15px;font-weight:500;color:var(--white);background:var(--orange)}
.btn-login{background:var(--white);color:var(--ink);font-weight:600}
.hero-title{left:81px;top:272px;font-size:44px;font-weight:500}
.lead{font-size:14.5px;line-height:26px;color:var(--muted)}
.section-title{left:0;width:1200px;text-align:center;font-size:33px;font-weight:600}
.card{position:absolute;top:897px;width:234px;height:207px;background:var(--white);border-radius:10px 10px 28px 10px;box-shadow:0 6px 18px rgba(0,0,0,.12);padding:0 30px}
.card-active{background:var(--orange);color:var(--white);box-shadow:none}
.card-icon{margin-top:30px;width:44px;height:44px;border-radius:50%;background:#e5ecf5;display:flex;align-items:center;justify-content:center}
.card-active .card-icon{background:rgba(255,255,255,.35)}
.card h3{margin-top:18px;font-size:16px;font-weight:600}
.card p{margin-top:10px;font-size:14px;line-height:26px;color:var(--muted)}
.card-active p{color:var(--white)}
.field{position:absolute;border:2px solid var(--field-line);border-radius:22px;background:var(--white);font-size:13.5px;color:#999;padding:10px 18px}
.contact-box{position:absolute;left:130px;top:2461px;width:938px;height:186px;background:var(--orange);border-radius:0 0 32px 0;color:var(--white);display:flex}
.contact-col{flex:1;text-align:center;padding-top:26px;border-right:1px solid rgba(255,255,255,.35);margin:20px 0}
.contact-col:last-child{border-right:none}
.contact-col{margin:0}
.contact-col .ring{width:44px;height:44px;border:2px solid var(--white);border-radius:50%;margin:0 auto;display:flex;align-items:center;justify-content:center}
.contact-col h4{margin-top:12px;font-size:17px;font-weight:500}
.contact-col p{margin-top:4px;font-size:14px;line-height:26px}
.social{position:absolute;top:2691px;width:40px;height:40px;border-radius:50%;border:2px solid var(--white)}
.social-fill{position:absolute;inset:9px;border-radius:50%;background:var(--white);opacity:.85}
.foot-link{position:absolute;top:2772px;color:var(--white);font-size:14px}
</style>
</head>
<body>

<svg class="shape" width="1200" height="2826" viewBox="0 0 1200 2826" aria-hidden="true">
  <polygon points="562,0 1200,0 1200,716 900,560" fill="var(--blue)"/>
  <polygon points="508,198 540,190 526,228" fill="var(--orange)"/>
  <polygon points="524,226 552,214 540,242" fill="var(--blue)"/>
  <polygon points="966,120 1024,120 980,170" fill="#5b9ad6"/>
  <polygon points="850,650 930,650 880,702" fill="#b7d3ef"/>
  <polygon points="0,814 320,876 115,1104 0,1104" fill="var(--blue)"/>
  <polygon points="1090,1340 1200,1300 1200,1560" fill="var(--orange-soft)"/>
  <polygon points="1078,1300 1200,1230 1200,1500" fill="var(--orange)"/>
  <polygon points="0,1760 85,1810 0,1969" fill="var(--orange-soft)"/>
  <polygon points="0,1730 85,1780 0,1930" fill="var(--orange)"/>
  <path d="M750,1790 L1200,1733 L1200,2157 L880,2085 Q780,2040 770,1960 Z" fill="var(--blue)"/>
  <polygon points="0,2459 1200,2572 1200,2826 0,2826" fill="var(--blue)"/>
</svg>

<!-- Header -->
<div class="abs brand" style="left:75px;top:34px"><span class="brand-dot"></span>Vortel Insight</div>
<nav class="nav">
  <a style="left:686px">Home</a>
  <a style="left:786px">About Us</a>
  <a style="left:897px">Contact Us</a>
</nav>
<div class="btn btn-login" style="left:1019px;top:38px;width:104px;height:39px">Log in</div>

<!-- Hero -->
<h1 class="abs hero-title">Vortel Insight</h1>
<p class="abs lead" style="left:79px;top:351px;width:360px">Lorem Ipsum is simply dummy text of the printing and typesetting industry.</p>
<div class="btn" style="left:77px;top:439px;width:145px;height:40px">Contact Now</div>
<div class="abs" role="img" aria-label="Photo of a smiling woman with glasses working at a laptop" style="left:610px;top:190px;width:320px;height:420px;border-radius:70px;transform:rotate(40deg);background:linear-gradient(160deg,#e9ecee,#c9b6a2 55%,#8a6a50)"></div>

<!-- Company focus -->
<h2 class="abs section-title" style="top:764px">Company Focus</h2>
<div class="card card-active" style="left:77px">
  <div class="card-icon"><svg width="24" height="24" viewBox="0 0 24 24"><circle cx="8" cy="9" r="3" fill="#fff"/><circle cx="16" cy="9" r="3" fill="#fff"/><rect x="5" y="14" width="14" height="5" rx="2" fill="#fff"/></svg></div>
  <h3>Techniques</h3><p>Lorem ipsum is simply dummy text of typesetting</p>
</div>
<div class="card" style="left:347px">
  <div class="card-icon"><svg width="24" height="24" viewBox="0 0 24 24"><path d="M12 20 L3 11 A5 5 0 0 1 12 5 A5 5 0 0 1 21 11 Z" fill="var(--orange)"/></svg></div>
  <h3>Relationships</h3><p>Lorem ipsum is simply dummy text of typesetting</p>
</div>
<div class="card" style="left:618px">
  <div class="card-icon"><svg width="24" height="24" viewBox="0 0 24 24"><path d="M6 4 V19 M3 16 L6 19 L9 16" stroke="var(--orange)" stroke-width="2" fill="none"/><path d="M12 6 H20 M12 11 H18 M12 16 H16" stroke="var(--orange)" stroke-width="2"/></svg></div>
  <h3>Attributes</h3><p>Lorem ipsum is simply dummy text of typesetting</p>
</div>
<div class="card" style="left:887px">
  <div class="card-icon"><svg width="24" height="24" viewBox="0 0 24 24"><circle cx="12" cy="12" r="3" fill="var(--orange)"/><circle cx="5" cy="5" r="2.5" fill="var(--orange)"/><circle cx="19" cy="5" r="2.5" fill="var(--orange)"/><circle cx="5" cy="19" r="2.5" fill="var(--orange)"/><circle cx="19" cy="19" r="2.5" fill="var(--orange)"/><path d="M5 5 L19 19 M19 5 L5 19" stroke="var(--orange)" stroke-width="1.5"/></svg></div>
  <h3>Activity Cluster</h3><p>Lorem ipsum is simply dummy text of typesetting</p>
</div>

<!-- Welcome -->
<h2 class="abs section-title" style="top:1222px;font-size:31px">Welcome To Vortel Insight</h2>
<p class="abs lead" style="left:270px;top:1287px;width:660px;text-align:center">Lorem Ipsum is simply dummy text of the printing and typesetting industry. Lorem Ipsum has been the industry's standard dummy text ever since the 1500s,</p>
<div class="abs" role="img" aria-label="Photo of two colleagues smiling at a laptop, with a video play button" style="left:158px;top:1375px;width:292px;height:304px;border-radius:0 0 0 50px;background:linear-gradient(135deg,#cfd3d6,#a88d74 60%,#3e4a5c)">
  <div class="abs" style="left:104px;top:112px;width:84px;height:84px;border-radius:50%;background:rgba(255,255,255,.55)"></div>
  <svg class="abs" style="left:134px;top:138px" width="30" height="32" viewBox="0 0 30 32"><polygon points="0,0 30,16 0,32" fill="var(--orange)"/></svg>
</div>
<div class="abs lead" style="left:503px;top:1383px;width:540px">
  <p>Lorem Ipsum is simply dummy text of the printing and typesetting industry. Lorem Ipsum has been the industry's standard dummy text ever since the 1500s, when an unknown printer took a galley of type and scrambled it to make a type specimen book.</p>
  <p style="margin-top:26px">It has survived not only five centuries, but also the leap into electronic typesetting, remaining essentially unchanged. It was popularised in the 1960s with the release of Letraset sheets containing.</p>
</div>
<div class="btn" style="left:501px;top:1628px;width:145px;height:39px">Learn More</div>

<!-- Contact -->
<h2 class="abs" style="left:79px;top:1828px;font-size:31px;font-weight:600">Contact Us</h2>
<p class="abs lead" style="left:79px;top:1893px;width:410px">Lorem Ipsum is simply dummy text of the printing and typesetting industry. Lorem Ipsum has been the industry's standard dummy text ever since the 1500s</p>
<div class="field" style="left:529px;top:1835px;width:291px;height:42px">Name*</div>
<div class="field" style="left:831px;top:1835px;width:292px;height:42px">E-mail*</div>
<div class="field" style="left:529px;top:1888px;width:291px;height:42px">Phone*</div>
<div class="field" style="left:831px;top:1888px;width:292px;height:42px">Subject</div>
<div class="field" style="left:529px;top:1942px;width:594px;height:70px;border-radius:30px">Message</div>
<div class="btn" style="left:529px;top:2023px;width:145px;height:40px">Submit Now</div>

<!-- Subscribe -->
<h2 class="abs section-title" style="top:2213px;font-size:31px">Subscribe Us</h2>
<p class="abs lead" style="left:0;width:1200px;top:2280px;text-align:center">For latest news or updates subscribe our newsletter</p>
<div class="field" style="left:367px;top:2336px;width:330px;height:40px;border:none;box-shadow:0 3px 14px rgba(0,0,0,.1);font-style:italic">Enter e-mail*</div>
<div class="btn" style="left:708px;top:2336px;width:145px;height:40px">Subscribe</div>

<!-- Footer -->
<div class="contact-box">
  <div class="contact-col">
    <div class="ring"><svg width="22" height="22" viewBox="0 0 24 24"><path d="M6 3 L10 7 L8 10 Q10 14 14 16 L17 14 L21 18 L18 21 Q10 20 3 6 Z" fill="#fff"/></svg></div>
    <h4>Call Us</h4><p>123 456 7890</p>
  </div>
  <div class="contact-col">
    <div class="ring"><svg width="22" height="22" viewBox="0 0 24 24"><path d="M12 22 Q4 13 4 9 A8 8 0 0 1 20 9 Q20 13 12 22 Z" fill="none" stroke="#fff" stroke-width="2"/><circle cx="12" cy="9" r="3" fill="#fff"/></svg></div>
    <h4>Address</h4><p>123, Lorem ipsum is simply<br>dummy text of tyesetting</p>
  </div>
  <div class="contact-col">
    <div class="ring"><svg width="22" height="22" viewBox="0 0 24 24"><rect x="3" y="6" width="18" height="13" rx="1" fill="#fff"/><path d="M3 6 L12 13 L21 6" stroke="var(--orange)" stroke-width="1.6" fill="none"/></svg></div>
    <h4>E-mail</h4><p>info@vortelinsight.com</p>
  </div>
</div>

<div class="social" style="left:526px" aria-label="Social profile 1"><div class="social-fill"></div></div>
<div class="social" style="left:581px" aria-label="Social profile 2"></div>
<div class="social" style="left:632px" aria-label="Social profile 3"></div>

<div class="abs brand" style="left:75px;top:2760px;color:var(--white)"><span class="brand-dot"></span>Vortel Insight</div>
<p class="abs" style="left:456px;top:2772px;font-size:14px;color:var(--white)">© VORTEL INSIGHT- 2018. All Rights Reserved.</p>
<span class="foot-link" style="left:852px">Home</span>
<span class="foot-link" style="left:914px">|</span>
<span class="foot-link" style="left:940px">About Us</span>
<span class="foot-link" style="left:1022px">|</span>
<span class="foot-link" style="left:1047px">Contact us</span>

</body>
</html>
```